Direct Response Coupon/Flyer for Trade Show

We are looking for something simple and quick. Using our logo and maybe some stock photos.
We need a call to action piece with the following
1. " Every $5,000 save $1,000"
2. Limited time offer. Must reserve your procedure by June 15th
3. content is the following : KBRV is a medical tourism company that facilitates wellness by connecting our clients with qualified medical practitioners in Medellin, Colombia offering dental, vision, cosmetic and other medical procedures.
4. full color 3.5x8.25
5. On the bottom near the left or right we need "Member of the Patient Voyage Alliance and the attached logo.
6. to speak to a case manger call 888-555-0173
7. our website is kbrv-example.com to get an idea of our brand and style
looking for something quick
We want the same style as the attached brochure

```html
<!DOCTYPE html>
<html lang="en">
<head>
<meta charset="utf-8">
<title>KBRV Trade Show Flyer</title>
<link rel="stylesheet" href="https://fonts.googleapis.com/css2?family=Oswald:wght@300;400;500&display=swap">
<style>
  :root {
    --teal: #14a3ad;
    --white: #ffffff;
    --black: #0b0b0b;
    --gold: #c8a24a;
    --grey: #bfbfbf;
    --stage: #e4e5e7;
  }
  * { margin: 0; padding: 0; box-sizing: border-box; }
  html, body {
    width: 1200px;
    height: 1200px;
    overflow: hidden;
    background: var(--stage);
    font-family: "Oswald", "Arial Narrow", sans-serif;
  }
  .flyer {
    position: absolute;
    left: 360px;
    top: 50px;
    width: 480px;
    height: 1100px;
    display: flex;
    flex-direction: column;
  }
  .offer {
    height: 494px;
    flex: none;
    background: var(--white);
    padding: 55px 44px 0;
    color: var(--teal);
  }
  .offer-headline {
    font-weight: 400;
    font-size: 74px;
    line-height: 130px;
    text-align: center;
    white-space: nowrap;
    letter-spacing: 0.5px;
  }
  .offer-headline span { display: block; }
  .offer-terms {
    margin-top: 18px;
    font-weight: 400;
    font-size: 25px;
    line-height: 54px;
    letter-spacing: 0.4px;
    white-space: nowrap;
  }
  .offer-terms span {
    display: block;
    text-align: justify;
    text-align-last: justify;
  }
  .offer-terms sup { font-size: 14px; }
  .about {
    height: 242px;
    flex: none;
    background: var(--teal);
    padding: 34px 56px 0 60px;
    color: var(--white);
  }
  .about-text {
    font-weight: 400;
    font-size: 21px;
    line-height: 36px;
    text-align: justify;
  }
  .contact-block {
    flex: 1;
    background: var(--black);
    position: relative;
  }
  .brand {
    position: absolute;
    left: 100px;
    top: 62px;
    display: flex;
    align-items: center;
    gap: 22px;
  }
  .brand-dot {
    width: 46px;
    height: 46px;
    border-radius: 50%;
    background: var(--teal);
  }
  .brand-name {
    color: var(--teal);
    font-weight: 300;
    font-size: 48px;
    letter-spacing: 3px;
  }
  .membership {
    position: absolute;
    left: 140px;
    top: 176px;
    display: flex;
    align-items: center;
    gap: 22px;
  }
  .membership-text {
    color: var(--gold);
    font-weight: 500;
    font-size: 15px;
    line-height: 1.45;
    text-align: right;
    text-transform: uppercase;
  }
  .membership-badge {
    width: 66px;
    height: 66px;
    border-radius: 50%;
    background: radial-gradient(circle at 40% 35%, #e2c57a, var(--gold) 55%, #8a6b27);
  }
  .footer {
    position: absolute;
    left: 58px;
    right: 24px;
    bottom: 52px;
    display: flex;
    align-items: center;
    color: var(--white);
    font-weight: 400;
    font-size: 13px;
    white-space: nowrap;
  }
  .footer-divider {
    width: 1px;
    height: 20px;
    background: var(--grey);
    margin: 0 9px;
  }
  .social-square {
    width: 13px;
    height: 13px;
    background: var(--grey);
    margin-right: 5px;
  }
</style>
</head>
<body>
  <main class="flyer">
    <section class="offer">
      <h1 class="offer-headline"><span>Every $5,000</span><span>save $1,000!</span></h1>
      <p class="offer-terms"><span>Limited time offer. Must reserve</span><span>your procedure by June 15<sup>th</sup>.</span></p>
    </section>
    <section class="about">
      <p class="about-text">KBRV is a medical tourism company that facilitates wellness by connecting our clients with qualified medical practitioners in Medellin, Colombia offering dental, vision, cosmetic and other medical procedures.</p>
    </section>
    <section class="contact-block">
      <div class="brand">
        <span class="brand-dot"></span>
        <span class="brand-name">KBRV</span>
      </div>
      <div class="membership">
        <p class="membership-text">Member of the<br>Patient Voyage Alliance</p>
        <span class="membership-badge" role="img" aria-label="Alliance membership badge"></span>
      </div>
      <div class="footer">
        <span>kbrv-example.com</span>
        <span class="footer-divider"></span>
        <span>to speak to a case manger call 888-555-0173</span>
        <span class="footer-divider"></span>
        <span class="social-square"></span>
        <span class="social-square"></span>
      </div>
    </section>
  </main>
</body>
</html>
```